Build a Web page - Dovin Pratchell Homes, LLC - a custom home builder

We are a custom home builder in Wisconsin. Need a basic web page with a home page, About Us, Contact info, Gallery, and Testimonials page. Gallery will probably have sub-pages and each will have about ten pictures or less. I already own the domain and have web hosting through Wix, I just need the site built. Once the page is built I should be able to do the upkeep on it myself. If I need to add pictures or whatever.
Updates

Project Deadline Extended
Reason: I am still looking through designs and will select soon - thank you!

Target Market(s)

Gen X and Millennials who are looking to build a home. Custom built homes - not generic spec homes.

Industry/Entity Type

Home Builder

Number of Pages Required

5+ page

Font styles to use
Sans Serif

Colors
ffffff
ec1f27
000000
9d9d9d

Requirements
Must have
• I have no idea if I want coded or in coded. I'm not sure of the difference and why I would want one over the other.
Nice to have
• We like the following colors - red, black, gray, white.
Should not have
• not a big fan of clip art like hammers, tape measures, etc. Must look professional.

```html
<!DOCTYPE html>
<html lang="en">
<head>
<meta charset="utf-8">
<title>Dovin Pratchell Homes, LLC</title>
<link rel="stylesheet" href="https://fonts.googleapis.com/css2?family=Oswald:wght@300;400;500&family=Raleway:ital,wght@0,300;0,400;0,500;0,700;1,400&display=swap">
<style>
:root{
  --red:#ec1f27;
  --black:#000000;
  --white:#ffffff;
  --gray:#9d9d9d;
  --gray-dark:#6b6b6b;
  --text:#5a5a5a;
  --quote-bg:#f2f2f2;
  --footer:#0d0d0d;
  --wood:#7a4a28;
  --wood-dark:#4a2c18;
  --wood-light:#a87a50;
}
*{margin:0;padding:0;box-sizing:border-box}
html,body{width:1200px;height:2647px;overflow:hidden;background:var(--white)}
body{position:relative;font-family:'Raleway',sans-serif;color:var(--text)}
.abs{position:absolute}

/* header */
.site-header{left:0;top:0;width:1200px;height:125px;background:var(--white)}
.brand{left:78px;top:18px;width:102px;height:92px;border:4px solid var(--gray-dark);display:flex;align-items:center;justify-content:center;text-align:center;font-family:'Oswald',sans-serif;font-weight:500;font-size:15px;line-height:18px;color:var(--red)}
.phone-tab{left:946px;top:0;width:177px;height:44px;background:var(--red);color:var(--white);font-family:'Oswald',sans-serif;font-size:17px;display:flex;align-items:center;justify-content:center;gap:10px}
.main-nav{left:482px;top:60px;display:flex;font-size:16px;color:#222;letter-spacing:.3px}
.main-nav a{color:inherit;text-decoration:none;height:44px;display:flex;align-items:center}
.nav-home{width:81px;justify-content:center;border:3px solid var(--gray)}
.nav-about{margin-left:44px}
.nav-gallery{margin-left:63px}
.nav-testimonials{margin-left:58px}
.nav-contact{margin-left:61px}

/* hero */
.hero{left:0;top:125px;width:1200px;height:551px;
  background:
    radial-gradient(ellipse 260px 200px at 560px 200px,rgba(230,225,215,.55),transparent 70%),
    linear-gradient(180deg,transparent 62%,rgba(40,25,15,.45) 100%),
    linear-gradient(90deg,#c9c2b4 0%,#7a4a28 6%,#8a5a34 20%,#a38a6c 36%,#cfc6b6 50%,#6e4326 64%,#9a6a40 78%,#b89a78 88%,#6a3f22 100%)}
.hero-title{left:0;top:290px;width:1200px;text-align:center;font-family:'Oswald',sans-serif;font-weight:400;font-size:58px;line-height:62px;color:var(--white);text-transform:uppercase;text-shadow:0 2px 6px rgba(0,0,0,.35)}
.btn-red{background:var(--red);color:var(--white);display:flex;align-items:center;justify-content:center;gap:12px;text-transform:uppercase;text-decoration:none}
.hero-cta{left:445px;top:450px;width:310px;height:56px;font-size:21px}

/* welcome */
.welcome-title{left:80px;top:712px;font-family:'Oswald',sans-serif;font-weight:400;font-size:48px;color:var(--black);text-transform:uppercase}
.welcome-title .accent{color:var(--red)}
.welcome-title .muted{color:var(--gray)}
.welcome-copy{left:80px;top:798px;width:662px;font-size:14.5px;font-weight:400;line-height:26.5px;letter-spacing:.15px;color:var(--text)}
.welcome-copy p+p{margin-top:26px}
.welcome-mark{left:822px;top:729px;width:300px;height:271px;border:6px solid var(--gray-dark);display:flex;align-items:center;justify-content:center}
.welcome-mark-inner{width:246px;height:217px;border:3px solid var(--gray-dark);display:flex;align-items:center;justify-content:center;gap:12px;font-weight:700;font-size:22px;color:var(--red);text-transform:uppercase;text-align:center}
.welcome-mark-inner .dot{width:14px;height:14px;background:var(--red);flex:none}

/* gallery */
.tile{position:absolute}
.g-living{left:0;top:1054px;width:247px;height:199px;background:
  linear-gradient(180deg,#e3ddd2 0%,#d6cdbd 45%,#8a6346 70%,#c8bca8 100%)}
.g-bath{left:0;top:1259px;width:247px;height:255px;background:
  linear-gradient(90deg,#2f3440 0%,#9a6a3c 12%,#b88452 45%,#8a5a32 70%,#3b4656 100%)}
.g-kitchen{left:254px;top:1054px;width:247px;height:253px;background:
  linear-gradient(180deg,#b07a48 0%,#c89868 35%,#6b4426 60%,#c99a66 100%)}
.g-dining{left:254px;top:1314px;width:247px;height:200px;background:
  linear-gradient(180deg,#d8d2c6 0%,#bcb4a6 40%,#6a3c2a 65%,#d4cfc6 100%)}
.g-vanity{left:508px;top:1054px;width:249px;height:199px;background:
  linear-gradient(180deg,#eceae6 0%,#d6d3cf 50%,#ffffff 70%,#b8b2aa 100%)}
.g-family{left:508px;top:1259px;width:249px;height:255px;background:
  linear-gradient(180deg,#e6ddd0 0%,#cbb9a0 40%,#6d4a36 65%,#c9baa6 100%)}
.g-exterior{left:764px;top:1054px;width:436px;height:460px;background:
  linear-gradient(180deg,#eeeff0 0%,#dcdcdc 30%,#8a7266 44%,#a59a8c 52%,#5e8a34 60%,#7aa84a 80%,#4f7a2c 100%)}
.g-frame{left:774px;top:1064px;width:416px;height:440px;border:2px solid var(--white)}
.gallery-cta{left:838px;top:1258px;width:288px;height:50px;font-size:21px}

/* testimonials */
.section-title{left:0;width:1200px;text-align:center;font-family:'Oswald',sans-serif;font-weight:400;font-size:48px;text-transform:uppercase}
.clients-title{top:1558px;color:var(--black)}
.quote{left:236px;top:1647px;width:729px;height:144px;background:var(--quote-bg);padding:22px 38px;text-align:center;font-size:13.5px;line-height:26px;color:var(--gray-dark)}
.quote-tip{left:586px;top:1791px}
.avatar{left:558px;top:1816px;width:84px;height:84px;border-radius:50%;background:linear-gradient(180deg,#e4e4e4 0%,#c8c8c8 55%,#3a3a3a 100%);border:3px solid #e8e8e8}
.client{left:0;top:1908px;width:1200px;text-align:center;font-size:14px;color:var(--gray-dark)}
.client .name{font-family:'Oswald',sans-serif;font-size:22px;color:var(--red)}
.client .place{font-style:italic}

/* contact */
.contact{left:0;top:1991px;width:1200px;height:595px;background:
  radial-gradient(ellipse 300px 220px at 420px 90px,rgba(120,90,70,.35),transparent 70%),
  radial-gradient(ellipse 260px 180px at 1100px 470px,rgba(130,70,60,.35),transparent 70%),
  linear-gradient(120deg,#4a3628 0%,#2a1f19 40%,#332519 70%,#4a3426 100%)}
.contact-title{top:2028px;color:var(--red)}
.col-title{font-family:'Oswald',sans-serif;font-weight:400;font-size:28px;color:var(--white)}
.form-title{left:80px;top:2095px}
.detail-title{left:623px;top:2095px}
.field{left:78px;width:499px;background:var(--white);padding:0 18px;font-size:13.5px;color:var(--gray);display:flex;align-items:center}
.f-name{top:2157px;height:53px;border:2px solid var(--red)}
.f-phone{top:2215px;height:53px}
.f-email{top:2273px;height:53px}
.f-message{top:2331px;height:132px;align-items:flex-start;padding-top:18px}
.submit{left:264px;top:2402px;width:124px;height:124px;border-radius:50%;background:var(--red);color:var(--white);font-family:'Oswald',sans-serif;font-size:28px;display:flex;align-items:center;justify-content:center;text-transform:uppercase}
.company{left:623px;top:2155px;color:var(--white);font-size:15px}
.company .firm{font-weight:700;text-transform:uppercase}
.company .addr{margin-top:8px;font-size:14px;color:#ddd}
.reach{left:623px;top:2212px;display:flex;align-items:center;gap:12px;color:var(--white);font-size:16px}
.reach .tel{font-weight:700}
.reach .mail{margin-left:44px;font-style:italic;display:flex;align-items:center;gap:12px}
.map{left:623px;top:2252px;width:499px;height:212px;background:
  linear-gradient(180deg,#e4e0d8 0%,#dcd8cf 100%)}
.map-pin{left:858px;top:2320px}
.follow{left:625px;top:2496px;color:var(--white);font-size:14px;font-weight:700}
.social{top:2485px;width:42px;height:42px;border-radius:50%;border:2px solid var(--white);display:flex;align-items:center;justify-content:center;font-size:10px;font-weight:700;color:var(--white)}
.s1{left:740px;background:var(--white);color:var(--red)}
.s2{left:789px}
.s3{left:839px}
.s4{left:888px}

/* footer */
.site-footer{left:0;top:2586px;width:1200px;height:61px;background:var(--footer);color:var(--white);font-family:'Oswald',sans-serif;font-size:15px;display:flex;align-items:center;justify-content:center}
.site-footer .accent{color:var(--red);margin:0 4px}
</style>
</head>
<body>

<header class="abs site-header">
  <div class="abs brand">Dovin<br>Pratchell<br>Homes</div>
  <div class="abs phone-tab">
    <svg width="18" height="18" viewBox="0 0 24 24"><path fill="#fff" d="M6.6 10.8c1.4 2.8 3.8 5.1 6.6 6.6l2.2-2.2c.3-.3.7-.4 1-.2 1.1.4 2.3.6 3.6.6.6 0 1 .4 1 1V20c0 .6-.4 1-1 1C10.6 21 3 13.4 3 4c0-.6.4-1 1-1h3.5c.6 0 1 .4 1 1 0 1.3.2 2.5.6 3.6.1.3 0 .7-.2 1z"/></svg>
    (01) 123 456 7890
  </div>
  <nav class="abs main-nav">
    <a class="nav-home">HOME</a>
    <a class="nav-about">ABOUT</a>
    <a class="nav-gallery">GALLERY</a>
    <a class="nav-testimonials">TESTIMONIALS</a>
    <a class="nav-contact">CONTACT</a>
  </nav>
</header>

<section>
  <div class="abs hero" role="img" aria-label="Photo of a custom kitchen with wood cabinets, tile backsplash and island with bar stools"></div>
  <h1 class="abs hero-title">We design for the<br>way you live.</h1>
  <a class="abs btn-red hero-cta">Get in touch with us
    <svg width="22" height="14" viewBox="0 0 22 14"><path d="M0 7h20M14 1l6 6-6 6" stroke="#fff" stroke-width="1.8" fill="none"/></svg>
  </a>
</section>

<section>
  <h2 class="abs welcome-title">Welcome to <span class="accent">Dovin</span><span class="muted">Pratchell</span></h2>
  <div class="abs welcome-copy">
    <p>Lorem Ipsum is simply dummy text of the printing and typesetting industry. Lorem Ipsum has been the industry's standard dummy text ever since the 1500s, when an unknown printer took a galley of type and scrambled it to make a type specimen book. It has survived not only five centuries, but also the leap into electronic typesetting, remaining essentially unchanged.</p>
    <p>It was popularised in the 1960s with the release of Letraset sheets containing Lorem Ipsum passages, and more recently with desktop publishing software like Aldus PageMaker including versions of Lorem Ipsum.</p>
  </div>
  <div class="abs welcome-mark">
    <div class="welcome-mark-inner"><span class="dot"></span>Dovin Pratchell<br>Homes</div>
  </div>
</section>

<section>
  <div class="tile g-living" role="img" aria-label="Photo of a living room with fireplace and built-in shelves"></div>
  <div class="tile g-bath" role="img" aria-label="Photo of a bathroom with wood vanity"></div>
  <div class="tile g-kitchen" role="img" aria-label="Photo of a kitchen with island and bar chairs"></div>
  <div class="tile g-dining" role="img" aria-label="Photo of a basement dining and family area"></div>
  <div class="tile g-vanity" role="img" aria-label="Photo of a white bathroom vanity"></div>
  <div class="tile g-family" role="img" aria-label="Photo of a family room with sectional sofa"></div>
  <div class="tile g-exterior" role="img" aria-label="Photo of a home exterior with lawn and young tree"></div>
  <div class="abs g-frame"></div>
  <a class="abs btn-red gallery-cta">View full gallery
    <svg width="22" height="14" viewBox="0 0 22 14"><path d="M0 7h20M14 1l6 6-6 6" stroke="#fff" stroke-width="1.8" fill="none"/></svg>
  </a>
</section>

<section>
  <h2 class="abs section-title clients-title">What clients say</h2>
  <blockquote class="abs quote">"Lorem Ipsum is simply dummy text of the printing and typesetting industry. Lorem Ipsum has been the industry's standard dummy text ever since the 1500s, when an unknown printer took a galley of type and scrambled it to make a type specimen book. It has survived not only five centuries, but also the leap into electronic typesetting, remaining essentially unchanged."</blockquote>
  <svg class="abs quote-tip" width="28" height="16" viewBox="0 0 28 16"><path d="M0 0h28L14 16z" fill="#f2f2f2"/></svg>
  <div class="abs avatar" role="img" aria-label="Client portrait photo"></div>
  <p class="abs client"><span class="name">Nolan R.,</span> <span class="place">Ashford-WI (Meadowline)</span></p>
</section>

<section>
  <div class="abs contact" role="img" aria-label="Dimmed photo of a furnished living room interior"></div>
  <h2 class="abs section-title contact-title">Contact us</h2>

  <h3 class="abs col-title form-title">Inquiry Form</h3>
  <div class="abs field f-name">Enter Name:</div>
  <div class="abs field f-phone">Enter Phone no.:</div>
  <div class="abs field f-email">Enter E-Mail:</div>
  <div class="abs field f-message">Message:</div>
  <div class="abs submit">Submit</div>

  <h3 class="abs col-title detail-title">Company Detail</h3>
  <div class="abs company">
    <div class="firm">Dovin Pratchell Homes</div>
    <div class="addr">123 Building Name, Area Name, City , Country - zipcode</div>
  </div>
  <div class="abs reach">
    <svg width="20" height="20" viewBox="0 0 24 24"><path fill="#ec1f27" d="M6.6 10.8c1.4 2.8 3.8 5.1 6.6 6.6l2.2-2.2c.3-.3.7-.4 1-.2 1.1.4 2.3.6 3.6.6.6 0 1 .4 1 1V20c0 .6-.4 1-1 1C10.6 21 3 13.4 3 4c0-.6.4-1 1-1h3.5c.6 0 1 .4 1 1 0 1.3.2 2.5.6 3.6.1.3 0 .7-.2 1z"/></svg>
    <span class="tel">123 456 7890</span>
    <span class="mail">
      <svg width="20" height="15" viewBox="0 0 20 15"><rect width="20" height="15" fill="#ec1f27"/><path d="M0 0l10 8 10-8" stroke="#fff" stroke-width="1.5" fill="none"/></svg>
      info@dovinpratchell.com
    </span>
  </div>
  <div class="abs map" role="img" aria-label="Street map showing the office location"></div>
  <svg class="abs map-pin" width="30" height="42" viewBox="0 0 30 42" aria-hidden="true"><path d="M15 0C6.7 0 0 6.7 0 15c0 11 15 27 15 27s15-16 15-27C30 6.7 23.3 0 15 0z" fill="#ec1f27"/><circle cx="15" cy="15" r="6" fill="#fff"/></svg>
  <div class="abs follow">Follow Us On :</div>
  <span class="abs social s1">Pli</span>
  <span class="abs social s2">Wren</span>
  <span class="abs social s3">Orb</span>
  <span class="abs social s4">Lux</span>
</section>

<footer class="abs site-footer">©<span class="accent">DOVINPRATCHELL Homes</span>- 2017. All Rights Reserved.</footer>

</body>
</html>
```